fry fang: flyer/menu board design for modern food van/trailer concept.

who are we? a modern food van/trailer selling restuarant quality food (burrito, burgers, waffles).our demographic is 16 - 35.

what do we need? a design for a flyer A4 size that is divided in 3 sections.with our menu on the inside and a design on the outside with our logo. the style must be funky, cool and modern.

Our restaurant theme is based on the movie "dusk blade" by marcus halloway. So any designs should be somehow linked to that genre.

the same menu on the flyer will be posted on our menu board. there is a chance we will use an lcd menu board so the format must accomodate that.
the menu must also be easilly modified in case we need to update changes pricing and menu items.

thank you
team fry fang

Hi, Project will become non-refundable as soon as i get some good designs. Thank you and good luck Team fry fang

Dear designers, I have uploaded some example menus, pics, my logo and hand drawings of my vision of how i would like the flyer/menu to look like. I understand that some designers cant see my uploads. I have contacted pixel forge and they are trying to fix the issue. The deadline will be extended if needed. Thank you for your patients and your designs. Regards, Rory

Hi, To those who are having trouble viewing my uploads, here is the link http://jobs.pixelforgehub.com/job.aspx?id=318560

Target Market(s)

our target market is young and cool between the ages of16 - 35. we are a multicultural society in a western governed country. Sydney Australia.

Industry/Entity Type

Restaurant

Font styles to use
Serif

Requirements
Must have
• pictures of menu items in a hand drawn black and white style: burger, burrito, waffles, buffallo wings, chicken, beef, prawn. examples provided
please feel free to show off your alternate ideas.
style should be modern, cool and funky. examples provided
Nice to have
• Colours: yellow, red, black.
Pictures/illustrations: black & white in a sketch style.
Theme: ninja, Mexican, modern, funky.

```html
<!DOCTYPE html>
<html lang="en">
<head>
<meta charset="utf-8">
<title>Fry Fang — Trifold Menu</title>
<link rel="stylesheet" href="https://fonts.googleapis.com/css2?family=Anton&family=Special+Elite&family=Patrick+Hand&family=Amatic+SC:wght@700&display=swap">
<style>
  :root {
    --page: #f4f4f2;
    --chalk: #2b2b2b;
    --chalk-deep: #1f1f1f;
    --chalk-text: #f1f1ee;
    --chalk-soft: #cfcfca;
    --heading: #d8c33c;
    --step-start: #f7a51c;
    --step-end: #d8222a;
    --heat: #e0532a;
    --cover-light: #f3ea4e;
    --cover-mid: #e2cf1e;
    --cover-dark: #c9ad0c;
    --ink: #141414;
    --notice-border: #e88b1c;
    --sketch: #4a4a4a;
  }
  * { box-sizing: border-box; margin: 0; padding: 0; }
  html, body { width: 947px; height: 1200px; overflow: hidden; background: var(--page); }
  body { position: relative; font-family: "Patrick Hand", cursive; color: var(--chalk-text); }

  /* ---------- inside spread ---------- */
  .spread {
    position: absolute; left: 131px; top: 22px;
    width: 684px; height: 560px;
    display: grid; grid-template-columns: repeat(3, 1fr);
    box-shadow: 0 6px 18px rgba(0,0,0,.25);
  }
  .panel {
    position: relative; overflow: hidden;
    padding: 9px 10px;
    background: radial-gradient(ellipse at 40% 35%, #333 0%, var(--chalk) 55%, var(--chalk-deep) 100%);
    border-right: 1px solid #151515;
    font-size: 9.5px; line-height: 1.15;
  }
  .panel:last-child { border-right: 0; }

  .section-title {
    font-family: "Special Elite", serif; font-weight: 700;
    color: var(--heading); font-size: 11px; letter-spacing: .5px;
  }
  .item-name {
    font-family: "Special Elite", serif; font-size: 10px;
    color: var(--chalk-text); letter-spacing: .4px;
  }
  .desc { font-size: 8.5px; color: var(--chalk-soft); }
  .blurb { font-size: 10px; color: var(--chalk-text); }

  .head-row { display: flex; align-items: flex-start; gap: 4px; }
  .head-row .text { flex: 1; }

  .sketch {
    flex: none; border-radius: 6px;
    background: linear-gradient(135deg, #555, var(--sketch));
    opacity: .8;
  }

  .tag {
    flex: none; position: relative; display: inline-block;
    border: 1.4px solid var(--chalk-text); border-radius: 3px;
    padding: 2px 6px 2px 11px; transform: rotate(-6deg);
    font-family: "Patrick Hand", cursive; font-size: 13px; color: var(--chalk-text);
  }
  .tag::before {
    content: ""; position: absolute; left: 3px; top: 50%;
    width: 4px; height: 4px; margin-top: -2px;
    border: 1px solid var(--chalk-text); border-radius: 50%;
  }

  .step {
    display: flex; align-items: center; gap: 7px;
    margin: 7px -10px 5px; padding: 3px 10px; height: 32px;
    background: linear-gradient(90deg, var(--step-start) 0%, var(--step-start) 28%, var(--step-end) 78%, rgba(216,34,42,0) 100%);
  }
  .step-num {
    font-family: "Anton", sans-serif; color: var(--step-end);
    font-size: 13px; line-height: .95; text-transform: uppercase;
  }
  .step-label {
    font-family: "Amatic SC", cursive; font-size: 21px;
    color: var(--chalk-text); text-transform: uppercase; letter-spacing: .5px;
  }

  .menu-item { margin-bottom: 4px; }
  .leader-row { display: flex; align-items: baseline; gap: 3px; margin-bottom: 4px; }
  .leader-row .leader { flex: 1; border-bottom: 1px dotted var(--chalk-soft); transform: translateY(-2px); }
  .leader-row .note { font-size: 8px; color: var(--chalk-soft); }
  .leader-row .heat { font-family: "Special Elite", serif; font-size: 9px; color: var(--heat); }
  .leader-row .price { font-family: "Special Elite", serif; font-size: 9.5px; }

  .filling-icons { display: flex; justify-content: space-between; margin: 4px 0 2px; }
  .filling-icons .sketch { width: 44px; height: 24px; }

  .meal { display: flex; align-items: center; gap: 5px; margin-top: 6px; }
  .meal .text { flex: 1; }
  .small-note { font-size: 8px; color: var(--chalk-soft); margin-bottom: 6px; }

  .pack-labels { display: flex; justify-content: space-around; font-size: 8.5px; margin-top: 4px; }
  .pack-tags { display: flex; justify-content: space-between; margin: 3px 0 8px; }
  .price-row { display: flex; align-items: center; justify-content: space-between; margin-bottom: 4px; }

  .notice {
    margin-top: 8px; padding: 10px 12px;
    border: 1.5px solid var(--notice-border);
    text-align: center; font-family: "Special Elite", serif; font-size: 9px; line-height: 1.35;
    position: relative;
  }
  .notice p + p { margin-top: 6px; }
  .notice .chili { position: absolute; width: 8px; height: 22px; border-radius: 4px; background: var(--step-end); }

  /* ---------- outside cover ---------- */
  .cover {
    position: absolute; left: 131px; top: 614px;
    width: 684px; height: 560px;
    display: grid; grid-template-columns: repeat(3, 1fr);
    background: radial-gradient(ellipse at 50% 50%, var(--cover-light) 0%, var(--cover-mid) 55%, var(--cover-dark) 100%);
    box-shadow: 0 6px 18px rgba(0,0,0,.25);
    overflow: hidden;
  }
  .cover-panel { position: relative; border-right: 1px solid rgba(0,0,0,.12); }
  .cover-panel:last-child { border-right: 0; }
  .cover-band { position: absolute; left: 0; width: 684px; height: 16px; background: var(--ink); }
  .cover-band.top { top: 28px; }
  .cover-band.top-thin { top: 52px; height: 5px; }
  .cover-band.bottom { bottom: 40px; }
  .cover-band.bottom-thin { bottom: 64px; height: 5px; }
  .star { position: absolute; border-radius: 50%; background: var(--ink); }
  .brand {
    position: absolute; left: 0; right: 0; top: 190px;
    font-family: "Special Elite", serif; font-weight: 400; color: var(--ink);
    font-size: 34px; line-height: 1; text-align: center; white-space: nowrap;
  }
</style>
</head>
<body>

<section class="spread" aria-label="Inside menu">
  <!-- burritos panel -->
  <div class="panel">
    <div class="head-row">
      <div class="text">
        <div class="section-title">BURRITOS</div>
        <div class="blurb">What is a burrito?<br>A Mexican kebab, mate</div>
      </div>
      <div class="sketch" style="width:56px;height:32px" role="img" aria-label="Hand drawn burrito sketch"></div>
      <span class="tag">$9</span>
    </div>

    <div class="step"><span class="step-num">Step<br>One</span><span class="step-label">Choose your style</span></div>
    <div class="menu-item"><div class="item-name">ORIGINAL</div><div class="desc">Lettuce, Salsa, Guacamole &amp; Sour Cream</div></div>
    <div class="menu-item"><div class="item-name">FAJITA</div><div class="desc">Grilled Capsicum &amp; Onion, Salsa, Guacamole &amp; Sour Cream</div></div>
    <div class="menu-item"><div class="item-name">CALIFORNIA</div><div class="desc">Fries, Cheese, Salsa, Guacamole &amp; Sour Cream</div></div>

    <div class="step"><span class="step-num">Step<br>Two</span><span class="step-label">Choose your filling</span></div>
    <div class="leader-row"><span class="item-name">MEXICAN CHICKEN</span><span class="leader"></span><span class="note">Marinated Breast Chicken</span></div>
    <div class="leader-row"><span class="item-name">CHIPOTLE STEAK</span><span class="leader"></span><span class="note">Juicy Chargrilled Steak</span></div>
    <div class="leader-row"><span class="item-name">FISH FILLET</span><span class="leader"></span><span class="note">Flash Fried</span></div>
    <div class="leader-row"><span class="item-name">SALUTE PRAWN</span><span class="leader"></span><span class="note">With Lemon &amp; Herb</span></div>
    <div class="filling-icons">
      <div class="sketch" role="img" aria-label="Chicken sketch"></div>
      <div class="sketch" role="img" aria-label="Steak sketch"></div>
      <div class="sketch" role="img" aria-label="Fish fillet sketch"></div>
      <div class="sketch" role="img" aria-label="Prawn sketch"></div>
    </div>

    <div class="step"><span class="step-num">Step<br>Three</span><span class="step-label">Add a sauce (optional)</span></div>
    <div class="leader-row"><span class="item-name">CORRIANDER &amp; LIME</span><span class="leader"></span><span class="heat">(MILD)</span></div>
    <div class="leader-row"><span class="item-name">CHIPOTLE</span><span class="leader"></span><span class="heat">(MEDIUM)</span></div>
    <div class="leader-row"><span class="item-name">HOT SAUCE</span><span class="leader"></span><span class="heat">(HOT)</span></div>
    <div class="leader-row"><span class="item-name">HABANNERO</span><span class="leader"></span><span class="heat">(INSANE)</span></div>
    <div class="leader-row"><span class="item-name">EXTRAS</span><span class="leader"></span><span class="price">$1</span></div>
    <div class="leader-row"><span class="item-name">GUACAMOLE</span><span class="leader"></span><span class="price">$2</span></div>
    <div class="leader-row"><span class="item-name">EXTRA FILLING</span><span class="leader"></span><span class="price">$3</span></div>

    <div class="meal">
      <div class="text"><div class="section-title">MAKE IT A MEAL</div><div class="blurb">Fries, Sauce and a Drink</div></div>
      <div class="sketch" style="width:34px;height:26px" role="img" aria-label="Drink and fries sketch"></div>
      <span class="tag">$4.50</span>
    </div>
  </div>

  <!-- burgers panel -->
  <div class="panel">
    <div class="head-row">
      <div class="text">
        <div class="section-title">BURGERS</div>
        <div class="blurb">Out of this world! A good burger is a messy burger!</div>
      </div>
      <div class="sketch" style="width:42px;height:32px" role="img" aria-label="Hand drawn burger sketch"></div>
      <span class="tag">$9</span>
    </div>

    <div class="head-row" style="margin-top:8px">
      <div class="text">
        <div class="section-title">BEEF</div>
        <div class="blurb">200 gram! You got beef wid dat?</div>
      </div>
      <div class="sketch" style="width:30px;height:24px;margin-right:30px" role="img" aria-label="Beef steak sketch"></div>
    </div>
    <div class="menu-item"><div class="item-name">CLASSIC BEEF</div><div class="desc">Lettuce, Tomato, Grilled Onion, BBQ Sauce</div></div>
    <div class="menu-item"><div class="item-name">AUSSIE BURGER</div><div class="desc">Lettuce, Tomato, Grilled Onion, Pineapple, Beef Rashes, BBQ Sauce</div></div>
    <div class="menu-item"><div class="item-name">AMERICAN</div><div class="desc">Coleslaw, Tomato, Fries, Pickles, Mayo, Ketchup</div></div>
    <div class="menu-item"><div class="item-name">CHEESE BURGER</div><div class="desc">Cheese, Pickles, Onion, Mustard, Ketchup, Mayo</div></div>
    <div class="menu-item"><div class="item-name">BACKYARD BURGER</div><div class="desc">Lettuce, Tomato, Cheese, Pickles, Onion, Mustard, Ketchup, Mayo</div></div>
    <div class="menu-item"><div class="item-name">SURF 'N' TURF</div><div class="desc">Lettuce, Tomato, Calamari, Harrissa Paste, Ketchup, Mayo</div></div>

    <div class="head-row" style="margin-top:8px">
      <div class="text">
        <div class="section-title">CHICKEN</div>
        <div class="blurb">Mmm chiiigen...</div>
      </div>
      <div class="sketch" style="width:34px;height:30px;margin-right:30px" role="img" aria-label="Chicken drumstick sketch"></div>
    </div>
    <div class="menu-item"><div class="item-name">CLASSIC CHICKEN</div><div class="desc">Crispy Chicken Tenders, Lettuce, Cheese, Feisty Mayo</div></div>
    <div class="menu-item"><div class="item-name">CHICKEN 'N' CHIPS</div><div class="desc">Crispy Chicken Tenders, Fries, Coleslaw, Cheese, Feisty Mayo</div></div>
    <div class="menu-item"><div class="item-name">MEXICAN</div><div class="desc">Grilled Chicken Breast, Lettuce, Salsa, Guacamole, Southwest Sauce</div></div>
    <div class="menu-item"><div class="item-name">PORTUGUESE</div><div class="desc">Grilled Chicken Breast, Lettuce, Cheese, Mayo, Peri Peri</div></div>
    <div class="menu-item"><div class="item-name">LEBANESE</div><div class="desc">Grilled Chicken Breast, Fries, Lebanese Pickles, Garlic Sauce</div></div>

    <div class="leader-row" style="margin-top:8px"><span class="item-name">EXTRAS</span><span class="leader"></span><span class="price">$1</span></div>
    <div class="leader-row"><span class="item-name">GUACAMOLE</span><span class="leader"></span><span class="price">$2</span></div>
    <div class="leader-row" style="margin-bottom:0"><span class="item-name">DOUBLE BEEF OR CHICKEN</span><span class="leader"></span><span class="price">$3</span></div>
    <div class="small-note">(Make sure you're hungry!)</div>

    <div class="meal">
      <div class="text"><div class="section-title">MAKE IT A MEAL</div><div class="blurb">Fries, Sauce and a Drink</div></div>
      <div class="sketch" style="width:34px;height:26px" role="img" aria-label="Drink and fries sketch"></div>
      <span class="tag">$4.50</span>
    </div>
  </div>

  <!-- sides panel -->
  <div class="panel">
    <div class="section-title">BUFFALO CHICKEN RIBS</div>
    <div class="blurb">Is when a buffalo makes love to a chicken... drenched in sauce and served with ranch.</div>

    <div class="head-row" style="margin-top:8px">
      <div class="text">
        <div class="section-title">SAUCES</div>
        <div class="desc">Lemon &amp; Herb, BBQ, Hot Sauce, Peri Peri</div>
      </div>
      <div class="sketch" style="width:18px;height:14px" role="img" aria-label="Sauce pot sketch"></div>
    </div>
    <div class="pack-labels"><span>6 Pack</span><span>12 Pack</span><span>24 Pack</span></div>
    <div class="pack-tags"><span class="tag">$4.95</span><span class="tag">$14.95</span><span class="tag">$7.95</span></div>

    <div class="head-row">
      <div class="text">
        <div class="section-title">NACHOS</div>
        <div class="blurb">Corn Chips 'n' Stuff</div>
      </div>
      <div class="sketch" style="width:44px;height:30px;margin-right:24px" role="img" aria-label="Nachos plate sketch"></div>
    </div>
    <div class="price-row"><div><div class="item-name">NACHOS GUACAMOLE</div><div class="desc">Guacamole, Sour Cream &amp; Cheese</div></div><span class="tag">$7</span></div>
    <div class="price-row"><div><div class="item-name">NACHOS BEEF</div><div class="desc">Corn Chips, Salsa, Beef Chilli,<br>Sour Cream &amp; Cheese</div></div><span class="tag">$7</span></div>
    <div class="price-row" style="justify-content:flex-start;gap:10px"><div><div class="item-name">MACHO NACHOS</div><div class="desc">All of the above</div></div><span class="tag">$9</span></div>

    <div class="price-row" style="margin-top:4px">
      <span class="section-title">FRIES</span>
      <div class="sketch" style="width:18px;height:18px" role="img" aria-label="Fries sketch"></div>
      <span class="tag">$4</span>
      <span style="flex:1"></span>
      <span class="tag">$10</span>
    </div>
    <div class="head-row">
      <div class="text">
        <div class="section-title">BELGIAN WAFFLES</div>
        <div class="blurb">(NOT FROZEN)</div>
      </div>
      <div class="sketch" style="width:40px;height:28px;margin-right:20px" role="img" aria-label="Waffle sketch"></div>
    </div>
    <div class="blurb" style="font-size:9px">House made waffles, freshly made while you wait!</div>
    <div class="desc">Served with fresh Strawberries, pure Maple Syrup, Belgian Chocolate and Fresh Cream. Enough said.</div>

    <div class="notice">
      <span class="chili" style="left:-5px;top:10px" role="img" aria-label="Chilli sketch"></span>
      <span class="chili" style="right:6px;bottom:30px" role="img" aria-label="Chilli sketch"></span>
      <p>We source and use the best quality ingredients and serve it the freshest way possible.</p>
      <p>All menu items have been prepared with care and are cooked while you wait.</p>
      <p>Please be patient as your food is being made.</p>
    </div>
  </div>
</section>

<section class="cover" aria-label="Outside cover">
  <div class="cover-band top"></div>
  <div class="cover-band top-thin"></div>
  <div class="cover-band bottom"></div>
  <div class="cover-band bottom-thin"></div>

  <div class="cover-panel">
    <div class="star" style="left:120px;top:110px;width:48px;height:48px" role="img" aria-label="Ninja throwing star"></div>
    <div class="star" style="left:-30px;top:280px;width:80px;height:80px" role="img" aria-label="Ninja throwing star"></div>
    <div class="star" style="left:150px;top:360px;width:40px;height:40px" role="img" aria-label="Ninja throwing star"></div>
  </div>
  <div class="cover-panel">
    <div class="star" style="left:150px;top:100px;width:22px;height:22px" role="img" aria-label="Ninja throwing star"></div>
    <div class="star" style="left:60px;top:200px;width:70px;height:70px" role="img" aria-label="Ninja throwing star"></div>
  </div>
  <div class="cover-panel">
    <div class="brand">Fry Fang</div>
    <div class="star" style="left:70px;top:340px;width:90px;height:90px" role="img" aria-label="Smoking ninja throwing star"></div>
  </div>
</section>

</body>
</html>
```